Velkano Holdings Ltd - An invesmtent & trading company needs a web design

We need a web design for our company based in Cyprus. The company was founded in 2009. We have continuously grown and now invest & trade all over the world.

Velkano Holdings ltd. specializes in the buying and selling of crude oil, precious metals and the investment in properties.

We know that trust is of the utmost importance when it comes to business and the design should communicate this to prospective business partners. Find attached the company logo. The colour scheme for the website should use similar colours and ideally incorporate the logo in some shape or form as well.

Target Market(s)

Oil Traders, Metall Traders, Property Investments

Industry/Entity Type

Trade

Coding

Coded - Design and coding required

Number of Pages Required

4 page

Font styles to use
Sans Serif

Requirements
Must have
• Mainpage,
• About Us
• Partners
• Legal Notice

```html
<!DOCTYPE html>
<html lang="en">
<head>
<meta charset="utf-8">
<title>Velkano Holdings Ltd</title>
<link href="https://fonts.googleapis.com/css2?family=Open+Sans:wght@400;600;700;800&display=swap" rel="stylesheet">
<style>
:root{
  --navy:#1c3a6b;
  --navy-dark:#0f2b52;
  --cyan:#1da4dc;
  --footer:#1aa6da;
  --grey-bg:#f1f2f4;
  --text:#6b7280;
  --white:#ffffff;
}
*{box-sizing:border-box;margin:0;padding:0}
html,body{width:694px;height:1200px;overflow:hidden}
body{font-family:'Open Sans',Arial,sans-serif;background:var(--white);color:var(--text);position:relative}
.site-header{height:42px;display:flex;align-items:center;padding:0 14px;background:var(--white)}
.brand{display:flex;align-items:center;gap:6px;width:230px}
.brand-mark{width:22px;height:22px;background:var(--navy)}
.brand-name{font-weight:800;font-size:11px;color:var(--navy);line-height:1.05;letter-spacing:.3px}
.main-nav{display:flex;gap:30px;margin-left:24px}
.main-nav a{font-size:6.5px;font-weight:700;color:var(--navy);text-decoration:none;position:relative;padding-top:4px}
.main-nav a.active::before{content:"";position:absolute;top:-3px;left:0;width:18px;height:3px;background:var(--cyan)}
.call{margin-left:auto;display:flex;align-items:center;gap:5px}
.call-icon{width:16px;height:16px;border-radius:50%;background:var(--cyan);display:flex;align-items:center;justify-content:center}
.call small{display:block;font-size:5px;color:var(--text)}
.call strong{display:block;font-size:7px;color:var(--cyan)}
.hero{position:relative;height:374px;background:linear-gradient(135deg,#5d6c80 0%,#8d9aab 35%,#b9c3cf 60%,#6f7e92 100%);text-align:center;color:var(--white)}
.hero h1{position:absolute;top:190px;left:0;right:0;font-size:25px;font-weight:800;letter-spacing:.5px}
.hero p{position:absolute;top:225px;left:180px;right:180px;font-size:8px;line-height:1.4}
.btn-light{position:absolute;top:262px;left:317px;width:60px;height:18px;background:var(--white);color:var(--navy);font-size:6px;font-weight:700;display:flex;align-items:center;justify-content:center}
.dots{position:absolute;top:352px;left:0;right:0;display:flex;justify-content:center;gap:5px}
.dots span{width:6px;height:6px;border-radius:50%;background:rgba(255,255,255,.5)}
.dots span.on{background:var(--white)}
.welcome{height:175px;text-align:center;padding-top:36px}
.section-title{font-size:17px;font-weight:800;color:var(--navy);letter-spacing:.3px}
.section-title em{font-style:normal;color:var(--cyan);font-weight:600}
.welcome p{margin:10px auto 0;width:600px;font-size:6.5px;line-height:1.55}
.btn-dark{display:inline-flex;margin-top:14px;width:58px;height:16px;background:var(--navy);color:var(--white);font-size:5.5px;font-weight:700;align-items:center;justify-content:center}
.services{height:318px;background:var(--grey-bg);text-align:center;padding-top:32px}
.services .intro{margin:8px auto 0;width:540px;font-size:6.5px;line-height:1.55}
.cards{display:flex;justify-content:center;gap:24px;margin-top:14px;text-align:left}
.card{width:190px}
.card-photo{height:112px}
.card h3{font-size:8px;color:var(--cyan);font-weight:600;margin-top:5px}
.card p{font-size:6px;line-height:1.5;margin-top:2px}
.card a{display:block;margin-top:8px;font-size:5.5px;color:var(--cyan);font-weight:700;text-decoration:none}
.partners{height:80px;display:flex;align-items:center;justify-content:center;gap:10px}
.arrow{width:14px;height:22px;background:#e4e6ea;display:flex;align-items:center;justify-content:center}
.partner{width:110px;height:34px;border:1px solid #e3e5e9;display:flex;align-items:center;justify-content:center}
.partner span{width:70px;height:14px;background:#c8ced7;border-radius:2px}
.site-footer{height:176px;background:var(--footer);color:var(--white);display:flex;padding:28px 26px 0;gap:22px}
.col h4{font-size:8px;font-weight:700;letter-spacing:.5px;margin-bottom:8px}
.col p{font-size:5.8px;line-height:1.55}
.col-about{width:168px}.col-news{width:166px}.col-loc{width:150px}.col-follow{width:90px}
.btn-outline{display:inline-flex;margin-top:10px;width:46px;height:15px;border:1px solid var(--white);font-size:5.5px;align-items:center;justify-content:center}
.email{margin-top:8px;height:15px;background:var(--white);color:#9aa3ad;font-size:5.5px;padding:4px 6px}
.subscribe{margin-top:5px;height:15px;background:#3a4a5c;font-size:5.5px;font-weight:700;display:flex;align-items:center;justify-content:center}
.info{display:flex;gap:5px;align-items:flex-start;font-size:5.8px;line-height:1.5;margin-bottom:6px}
.dot-icon{flex:none;width:9px;height:9px;border-radius:50%;background:var(--white)}
.social{display:flex;align-items:center;gap:6px;font-size:6.5px;margin-bottom:9px}
.bottom-bar{height:35px;background:var(--navy-dark);color:#9fb1c8;font-size:5.5px;display:flex;align-items:center;justify-content:center}
</style>
</head>
<body>
<header class="site-header">
  <div class="brand"><span class="brand-mark"></span><span class="brand-name">VELKANO<br>HOLDINGS LTD</span></div>
  <nav class="main-nav">
    <a class="active" href="#">HOME</a><a href="#">ABOUT US</a><a href="#">PARTNERS</a><a href="#">LEGAL NOTICE</a>
  </nav>
  <div class="call">
    <span class="call-icon"><svg width="8" height="8" viewBox="0 0 24 24"><path fill="#fff" d="M6.6 10.8a15 15 0 006.6 6.6l2.2-2.2a1 1 0 011-.2 11 11 0 003.6.6 1 1 0 011 1V20a1 1 0 01-1 1A17 17 0 013 4a1 1 0 011-1h3.5a1 1 0 011 1 11 11 0 00.6 3.6 1 1 0 01-.3 1z"/></svg></span>
    <div><small>CALL US</small><strong>+357 555 0142</strong></div>
  </div>
</header>

<section class="hero" role="img" aria-label="Business people reviewing financial documents at a desk">
  <h1>LOREM IPSUM DOLOR SIT AMET</h1>
  <p>Lorem ipsum dolor sit amet, consectetur adipiscing elit, sed do eiusmod tempor incidunt ut labore et dolore magna aliqua. Ut enim ad minim veniam, quis nostrud exercitation.</p>
  <span class="btn-light">READ MORE</span>
  <div class="dots"><span class="on"></span><span></span><span></span></div>
</section>

<section class="welcome">
  <h2 class="section-title">WELCOME TO <em>VELKANO HOLDINGS LTD</em></h2>
  <p>Lorem ipsum dolor sit amet, consectetur adipiscing elit, sed do eiusmod tempor incididunt ut labore et dolore magna aliqua. Ut enim ad minim veniam, quis nostrud exercitation ullamco laboris nisi ut aliquip ex ea commodo consequat. Duis aute irure dolor in reprehenderit in voluptate velit esse cillum dolore eu fugiat nulla pariatur. Excepteur sint occaecat cupidatat non proident, sunt in culpa qui officia deserunt mollit anim id est laborum.</p>
  <span class="btn-dark">READ MORE</span>
</section>

<section class="services">
  <h2 class="section-title">OUR <em>SERVICES</em></h2>
  <p class="intro">Lorem ipsum dolor sit amet, consectetur adipiscing elit, sed do eiusmod tempor incididunt ut labore et dolore magna aliqua. Ut enim ad minim veniam, quis nostrud exercitation ullamco laboris nisi ut aliquip.</p>
  <div class="cards">
    <article class="card">
      <div class="card-photo" role="img" aria-label="Crude oil pipeline valve" style="background:linear-gradient(135deg,#d8dadd,#9a9ea4 60%,#b8262a)"></div>
      <h3>Crude Oil</h3>
      <p>Lorem ipsum dolor sit amet, consectetur adipiscing elit, sed do eiusmod tempor incididunt ut labore.</p>
      <a href="#">READ MORE</a>
    </article>
    <article class="card">
      <div class="card-photo" role="img" aria-label="Stacked gold bars" style="background:linear-gradient(135deg,#f3d77a,#c99a2e 55%,#8a6318)"></div>
      <h3>Precious Metals</h3>
      <p>Lorem ipsum dolor sit amet, consectetur adipiscing elit, sed do eiusmod tempor incididunt ut labore.</p>
      <a href="#">READ MORE</a>
    </article>
    <article class="card">
      <div class="card-photo" role="img" aria-label="Small house model with keys" style="background:linear-gradient(135deg,#ffffff,#e9d2c6 55%,#b8503c)"></div>
      <h3>Investment in Properties</h3>
      <p>Lorem ipsum dolor sit amet, consectetur adipiscing elit, sed do eiusmod tempor incididunt ut labore.</p>
      <a href="#">READ MORE</a>
    </article>
  </div>
</section>

<section class="partners" aria-label="Partners">
  <span class="arrow"><svg width="6" height="8" viewBox="0 0 6 8"><path d="M5 0L1 4l4 4" fill="none" stroke="#7a8290" stroke-width="1.4"/></svg></span>
  <span class="partner"><span></span></span>
  <span class="partner"><span></span></span>
  <span class="partner"><span></span></span>
  <span class="partner"><span></span></span>
  <span class="partner"><span></span></span>
  <span class="arrow"><svg width="6" height="8" viewBox="0 0 6 8"><path d="M1 0l4 4-4 4" fill="none" stroke="#7a8290" stroke-width="1.4"/></svg></span>
</section>

<footer class="site-footer">
  <div class="col col-about">
    <h4>ABOUT US</h4>
    <p>Lorem ipsum dolor sit amet, consectetur adipiscing elit, sed do eiusmod tempor incididunt ut labore et dolore magna aliqua. Ut enim ad minim veniam, quis nostrud exercitation.</p>
    <span class="btn-outline">Read More</span>
  </div>
  <div class="col col-news">
    <h4>NEWSLETTER SIGNUP</h4>
    <p>Subscribe to our newsletter to receive our latest market news and updates.</p>
    <div class="email">Your email address</div>
    <div class="subscribe">SUBSCRIBE</div>
  </div>
  <div class="col col-loc">
    <h4>LOCATION</h4>
    <div class="info"><svg width="9" height="11" viewBox="0 0 24 30"><path fill="#fff" d="M12 0a10 10 0 00-10 10c0 8 10 20 10 20s10-12 10-20A10 10 0 0012 0zm0 14a4 4 0 110-8 4 4 0 010 8z"/></svg><span>Velkano Tower, 14 Harbour Road<br>Limassol, Cyprus 3036</span></div>
    <div class="info"><span class="dot-icon"></span><span>+357 25 555 014</span></div>
    <div class="info"><span class="dot-icon"></span><span>info@velkano.example</span></div>
  </div>
  <div class="col col-follow">
    <h4>FOLLOW US</h4>
    <div class="social"><span class="dot-icon"></span>Friendbook</div>
    <div class="social"><span class="dot-icon"></span>Chirper</div>
    <div class="social"><span class="dot-icon"></span>WorkLink</div>
  </div>
</footer>
<div class="bottom-bar">Copyright © Velkano Holdings ltd. All rights reserved</div>
</body>
</html>
```